Halt and Thicken New Branding Stationary Set - updated Oct 30th 2017

Updated on 30th Oct 2017 as we now need a whole folder design instead of a folder cover. We have thought out exactly what should be on it so it wont be hard. We are happy for this to be completed only by the winning designer if you like. And also we are guaranteeing this project now. Thanks!

We just got our new logo and now we would like a stationary set so we can brand our company communications. The items we need designed are:
Business cards
Letterhead
Appointment confirmation cards
Folder - switched from folder cover. Note that if you don't wish to do this unless you are selected as the winner this is fine.

1. Business cards - for 5 employees, final names will be given once the winner is selected, but you can use this one as the sample:
Lucinda Prieto
Hair Regrowth Expert
Halt and Thicken
7127 Marbury Ave, Suite 500
Kestrel Park CA 90877
lucinda@gavinthorpemd.example
(555) 238-9016

2. Letterhead 8.5" x 11.0" vertical
Halt and Thicken
Kestrel Park CA 90877
office@haltandthicken.example
(555) 238-9016

3. Appointment Confirmation cards - business card size
Halt and Thicken
Kestrel Park CA 90877
Appointment For:
Date:
Time:
If you are unable to make your appointment, please contact us to reschedule at:
(555) 238-9016
info@gavinthorpemd.example

*UPDATED*
4. Folder 9" x 12 " vertical with double pocket
We would like the infinity image from the logo made really big so the left side is on the back and the right side with the + sign is on the front and its takes up the maximum room on the folder.
On the front below the half logo it should say "A Biochemical Revolution..."
On the inside we would also like to have the infinity sign from the logo but faded and half on the left pocket half on the right.
On left inside pocket it should say (this will be partically written on top of the logo):
Gavin Thorpe MD
Precision Medicine
Halt and Thicken Hair
On the Right inside pocket it should say the following:
Because the Enemy of BETTER Health is Good Health
BETTER Ingredients
BETTER Recipe
BETTER Medicine
On the back below the logo on the bottom should be the contact information.
I attached a picture of our drawing of what we want for this to make it easier.

Here is our website to give you an idea of our branding: http://www.haltandthicken.example/

We are the only true cure for hair loss and need to look professional and highest quality and beyond reproach from an ethical standpoint. We are a medical clinic so this should be portrayed also.
We cured hair loss by analyzing biochemistry and rebalancing it so that the process reverses and your own hair can grow back naturally.

Business card information:

OK so here is the information for the business cards:

Lucinda Prieto
Hair Regrowth Expert
(555) 238-9016
www.haltandthicken.example

Marisol Quintero
Hair Growth Consultant
(555) 238-9016
marisol@gavinthorpemd.example
www.haltandthicken.example

Glenda Hutchins
CMO/COO
(555) 238-9016
glenda@haltandthicken.example
www.haltandthicken.example

Dr Lou Thorpe
President
(555) 238-9016
info@gavinthorpemd.example
www.haltandthicken.example

Halt and Thicken
Customer Service
(555) 238-9016
info@gavinthorpemd.example
www.haltandthicken.example

Target Market(s)

Men aged 20-24 who care about their appearance, care about their hair and care about the world.

Industry/Entity Type

Medical And Science

Font styles to use
Sans Serif

Colors
00a990
ffffff
9d9d9d
333333

Requirements
Must have
• Must use the logo and our brand colors from the logo in all designs.
• The pantone colors are:
• Green: #4ca26f
• Light Grey: #999999
• The design should be symmetrical and balanced.
Nice to have
• It should look reasonably masculine.
Should not have
• Do not include any red in the design.

```html
<!DOCTYPE html>
<html lang="en">
<head>
<meta charset="utf-8">
<title>Halt and Thicken – Business Card</title>
<link href="https://fonts.googleapis.com/css2?family=Open+Sans:wght@400;600;700&family=Questrial&display=swap" rel="stylesheet">
<style>
  :root {
    --green: #4ca26f;
    --green-deep: #1f7a4a;
    --green-light: #86cfa3;
    --grey: #999999;
    --grey-band: #eeeeee;
    --ink: #333333;
    --muted: #666666;
    --white: #ffffff;
    --stage: #e4e9e6;
  }
  * { box-sizing: border-box; margin: 0; padding: 0; }
  html, body { width: 1200px; height: 856px; overflow: hidden; }
  body {
    background: var(--stage);
    font-family: "Open Sans", Arial, sans-serif;
    display: flex;
    align-items: center;
    justify-content: center;
    gap: 40px;
  }
  .card {
    position: relative;
    width: 540px;
    height: 309px;
    border-radius: 24px;
    overflow: hidden;
  }
  .card svg.card-art { position: absolute; inset: 0; }

  /* Back side */
  .card-back {
    background: linear-gradient(160deg, var(--green-light) 0%, var(--green) 45%, var(--green-deep) 100%);
    color: var(--white);
    display: flex;
    flex-direction: column;
    align-items: center;
    justify-content: center;
    gap: 22px;
  }
  .brand-mark { display: flex; align-items: center; gap: 12px; }
  .brand-dot {
    width: 22px; height: 22px; border-radius: 50%;
    background: var(--white);
  }
  .brand-name-back {
    font-weight: 600;
    font-size: 34px;
    letter-spacing: 0.5px;
    text-transform: uppercase;
  }
  .back-url { font-weight: 600; font-size: 15px; letter-spacing: 0.3px; }

  /* Front side */
  .card-front { background: var(--white); }
  .front-brand {
    position: absolute;
    right: 34px; top: 72px;
    display: flex; align-items: center; gap: 8px;
  }
  .front-brand .brand-dot { width: 14px; height: 14px; background: var(--green); }
  .brand-name-front {
    font-weight: 600; font-size: 19px; color: var(--green);
    text-transform: uppercase; letter-spacing: 0.3px;
  }
  .holder { position: absolute; left: 30px; top: 150px; }
  .holder-name { font-weight: 700; font-size: 23px; color: var(--green); line-height: 28px; }
  .holder-role {
    font-family: "Questrial", Arial, sans-serif;
    font-variant: small-caps; font-size: 16px; color: #777;
    letter-spacing: 0.4px; line-height: 18px;
  }
  .contacts {
    position: absolute; left: 222px; top: 188px;
    font-size: 9.5px; line-height: 19px;
    white-space: nowrap;
  }
  .contact-row { display: flex; align-items: center; gap: 6px; }
  .contact-row svg { width: 12px; height: 12px; flex: none; }
  .contact-address { color: var(--green); font-weight: 700; }
  .contact-muted { color: var(--muted); }
  .contact-row .spacer { width: 8px; }
</style>
</head>
<body>

  <section class="card card-back" aria-label="Business card, back">
    <div class="brand-mark">
      <span class="brand-dot"></span>
      <span class="brand-name-back">Halt and Thicken</span>
    </div>
    <p class="back-url">www.haltandthicken.example</p>
  </section>

  <section class="card card-front" aria-label="Business card, front">
    <svg class="card-art" width="540" height="309" viewBox="0 0 540 309" aria-hidden="true">
      <rect class="header-band" x="0" y="50" width="540" height="70" fill="var(--grey-band)"/>
      <line class="rule" x1="212" y1="178" x2="504" y2="178" stroke="#9d9d9d" stroke-width="1"/>
      <rect class="rule-end" x="502" y="145" width="6" height="6" fill="var(--green)"/>
      <rect class="footer-stripe" x="0" y="252" width="340" height="5" fill="var(--green-deep)"/>
      <path class="footer-band" d="M330 266 Q330 250 346 250 H540 V309 H330 Z" fill="var(--green)"/>
      <path class="footer-band-shade" d="M330 266 Q330 250 346 250 H540 V258 H348 Q336 258 336 272 V309 H330 Z" fill="var(--green-deep)" opacity="0.35"/>
    </svg>

    <div class="front-brand">
      <span class="brand-dot"></span>
      <span class="brand-name-front">Halt and Thicken</span>
    </div>

    <div class="holder">
      <p class="holder-name">Lucinda Prieto</p>
      <p class="holder-role">Hair Regrowth Expert</p>
    </div>

    <div class="contacts">
      <p class="contact-row contact-address">
        <svg viewBox="0 0 12 12"><circle cx="6" cy="6" r="5.5" fill="none" stroke="var(--green)"/><path d="M6 2.5a2 2 0 0 0-2 2c0 1.6 2 4 2 4s2-2.4 2-4a2 2 0 0 0-2-2z" fill="var(--green)"/></svg>
        7127 Marbury Ave, Suite 500, Kestrel Park CA 90877
      </p>
      <p class="contact-row contact-muted">
        <svg viewBox="0 0 12 12"><circle cx="6" cy="6" r="5.5" fill="none" stroke="var(--green)"/><path d="M3.5 4.5h5l-.6 3.5h-3.8z" fill="var(--green)"/></svg>
        (555) 238-9016
        <span class="spacer"></span>
        <svg viewBox="0 0 12 12"><circle cx="6" cy="6" r="5.5" fill="none" stroke="var(--green)"/><rect x="3" y="4" width="6" height="4" fill="var(--green)"/></svg>
        lucinda@gavinthorpemd.example
      </p>
    </div>
  </section>

</body>
</html>
```